Filmmaking Collaboration Course Flyer

I need a flyer, either A4 (1 page - though there may be too much copy for 1 page) or square size (2 pages) to promote our Filmmaking Collaboration Course. We run innovative, creative training for corporate clients. We are a well-renowned video production company with film professionals who have created a unique event that delivers team building and collaboration skills.
Photo-wise, I have some credit with Pixelharbor, so please use this site if possible. Images of a camera filming, but also group images of people co-operating in a staged or film environment, looking like they're having fun. We could also use people who look like they're developing a story board.

The copy for the flyer is in the below Word document, titled Video Collaboration Course.

I have included a recent flyer we have had designed (Collaboration Skills PDF). It would be good to have the new one fit in with this style but not be exactly the same.

Please use the Quillmere Studios logo.

Target Market(s)

Corporate Market, Medium to Large Businesses

Font styles to use
Sans Serif

Requirements
Must have
• 2-3 photos
• Quillmere colours to fit with Collaboration Skills brochure

```html
<!DOCTYPE html>
<html lang="en">
<head>
<meta charset="utf-8">
<title>Filmmaking Collaboration Course Flyer</title>
<link href="https://fonts.googleapis.com/css2?family=Oswald:wght@300;400&family=Open+Sans:ital,wght@0,400;1,600&display=swap" rel="stylesheet">
<style>
  :root {
    --lime: #a9c43a;
    --forest: #11865f;
    --sky: #1ea0dc;
    --ink: #1f1f1f;
    --body: #555555;
    --rule: #c9c9c9;
    --green-head: #2f9a4a;
    --brand-teal: #2d8c8a;
    --paper: #ffffff;
  }
  * { box-sizing: border-box; margin: 0; padding: 0; }
  html, body { width: 1200px; height: 848px; overflow: hidden; background: var(--paper); }
  .flyer { position: relative; width: 1200px; height: 848px; background: var(--paper); font-family: "Open Sans", Arial, sans-serif; color: var(--body); }
  .page { position: absolute; top: 0; width: 600px; height: 848px; }
  .page--inside { left: 0; border-right: 1px solid #222; }
  .page--cover { left: 600px; }

  .section-title { position: absolute; font-family: "Oswald", "Arial Narrow", sans-serif; font-weight: 400; color: var(--ink); font-size: 19px; }
  .section-rule { position: absolute; height: 3px; background: var(--rule); }
  .skill-title { position: absolute; left: 42px; font-family: "Oswald", "Arial Narrow", sans-serif; font-weight: 400; color: var(--green-head); font-size: 19px; }
  .copy { position: absolute; font-size: 12.1px; line-height: 18px; color: var(--body); }

  .photo { position: absolute; }
  .photo--team-table { left: 58px; top: 515px; width: 484px; height: 258px; border-radius: 240px 240px 0 0 / 200px 200px 0 0;
    background: radial-gradient(ellipse at 50% 100%, #ffffff 0 45%, #dcd7d0 60%, #9a8f86 85%, #6c6a70 100%); }
  .contact { position: absolute; left: 182px; top: 645px; width: 218px; text-align: center; font-size: 12.6px; line-height: 19px; color: #111; }
  .contact__lines { font-style: italic; font-weight: 600; margin-top: 14px; }

  .brand-name { position: absolute; font-family: "Oswald", "Arial Narrow", sans-serif; font-weight: 400; color: var(--brand-teal); font-size: 26px; line-height: 1; }
  .brand-name--footer { left: 230px; top: 772px; }
  .brand-name--header { left: 40px; top: 100px; }

  .header-shapes { position: absolute; left: 0; top: 0; }
  .cover-title { position: absolute; left: 0; top: 6px; width: 600px; text-align: center; font-family: "Oswald", "Arial Narrow", sans-serif; font-weight: 400; color: #fff; font-size: 38px; line-height: 44px; }
  .cover-kicker { position: absolute; left: 235px; top: 50px; font-family: "Oswald", "Arial Narrow", sans-serif; color: #fff; font-size: 17px; font-weight: 400; }
  .cover-tagline { position: absolute; left: 240px; top: 78px; font-family: "Oswald", "Arial Narrow", sans-serif; color: #fff; font-size: 24px; font-weight: 400; }
  .cover-strap { position: absolute; left: 260px; top: 120px; font-family: "Oswald", "Arial Narrow", sans-serif; color: #fff; font-size: 20px; font-style: italic; font-weight: 400; }

  .photo--team-circle { left: 55px; top: 150px; width: 510px; height: 290px; border-radius: 0 0 255px 255px / 0 0 150px 150px;
    background: radial-gradient(ellipse at 50% 40%, #ffffff 0 40%, #cfd4d8 58%, #7b8792 80%, #4e5865 100%); }

  .cover-copy { left: 26px; top: 449px; width: 544px; text-align: justify; font-size: 12.4px; line-height: 16px; }
  .cover-copy p + p { margin-top: 16px; }
  .results { position: absolute; left: 28px; top: 646px; width: 550px; list-style: none; font-size: 12.4px; line-height: 18px; color: var(--body); }

  .base-bands { position: absolute; left: 0; bottom: 0; width: 1200px; height: 28px; }
  .base-bands span { display: block; width: 100%; }
  .band--lime { height: 11px; background: var(--lime); }
  .band--forest { height: 8px; background: var(--forest); }
  .band--sky { height: 9px; background: var(--sky); }
</style>
</head>
<body>
<main class="flyer">

  <section class="page page--inside">
    <h2 class="section-title" style="left:42px; top:20px;">YOUR TEAM WILL LEARN NEW CREATIVE SKILLS</h2>
    <div class="section-rule" style="left:0; top:49px; width:600px;"></div>

    <h3 class="skill-title" style="top:57px;">Collaboration</h3>
    <div class="copy" style="left:42px; top:82px; width:548px;">
      <p>• Discover the personal attributes needed for successful collaboration</p>
      <p>• Learn practical skills, from positive body language to listening with empathy to become better collaborators</p>
      <p>• Move away from the silo mentality and build trust</p>
    </div>

    <h3 class="skill-title" style="top:166px;">Brainstorming Techniques</h3>
    <div class="copy" style="left:42px; top:191px; width:540px;">
      <p>• Learn simple, fast brainstorming skills to develop your film topic</p>
      <p>• Develop a script and storyboard as a team</p>
    </div>

    <h2 class="section-title" style="left:46px; top:246px;">Filmmaking</h2>
    <div class="section-rule" style="left:0; top:276px; width:600px;"></div>
    <div class="copy" style="left:46px; top:290px; width:540px;">
      <p>Assign film roles including Director, Writers, Actors, Camera &amp; Sound and work with filmmaking professionals who guide you through the practical filmmaking processes to achieve a genuinely great result. All filming gear is supplied for the day.</p>
    </div>

    <h2 class="section-title" style="left:46px; top:355px;">WORK WITH PROFESSIONAL FILMMAKERS &amp; COACHES</h2>
    <div class="section-rule" style="left:0; top:386px; width:600px;"></div>
    <div class="copy" style="left:46px; top:399px; width:548px;">
      <p>Quillmere Studios was established in 2000 and works with a broad range of clients all over Australia as a professional production company to tell stories using the video medium. View our work here. www.quillmerestudios.com</p>
      <p>These skills are combined with the training experience of our sister company Quillmere Presentations to develop this truly unique team-building event. www.quillmerepresentations.com</p>
    </div>

    <div class="photo photo--team-table" role="img" aria-label="Overhead photo of a diverse business team standing around a round white table"></div>
    <div class="contact">
      <p>Call or email us to discuss your team’s needs. A range of venues and group size options are available.</p>
      <p class="contact__lines">info@quillmerestudios.com<br>(08) 5550 0142</p>
    </div>

    <p class="brand-name brand-name--footer">Quillmere Studios</p>
  </section>

  <section class="page page--cover">
    <svg class="header-shapes" width="600" height="152" viewBox="0 0 600 152" aria-hidden="true">
      <rect x="0" y="0" width="600" height="72" fill="var(--lime)"/>
      <rect x="0" y="72" width="600" height="42" fill="var(--forest)"/>
      <rect x="0" y="116" width="600" height="34" fill="var(--sky)"/>
      <path d="M0 78 L190 78 Q232 80 240 116 Q246 148 262 152 L0 152 Z" fill="#ffffff"/>
    </svg>
    <h1 class="cover-title">FILMMAKING COLLABORATION COURSE</h1>
    <p class="cover-kicker">Produce a film in one day with your team</p>
    <p class="cover-tagline">A team building event like no other</p>
    <p class="cover-strap">A creative alternative with a tangible outcome</p>

    <p class="brand-name brand-name--header">Quillmere Studios</p>

    <div class="photo photo--team-circle" role="img" aria-label="Overhead photo of business people holding hands around a white table with the word collaboration"></div>

    <div class="copy cover-copy">
      <p>Filmmaking is the ultimate exercise in creative collaboration: people from different backgrounds with different skills coming together for a common purpose.</p>
      <p>Quillmere Studios ‘Filmmaking Collaboration Course’ improves your team’s ability to work together creatively and to think laterally, and it provides a dynamic framework to build on individual’s strengths and skills. Each team will create a film about a product, service, personal story, or just about anything. It’s a fun and focused way to get your team working in unison. The results will give you an amazing insight to your team dynamics.</p>
    </div>

    <h2 class="section-title" style="left:28px; top:603px;">THE ASTONISHING RESULTS</h2>
    <div class="section-rule" style="left:0; top:634px; width:600px;"></div>
    <ol class="results">
      <li>1. The team’s video is edited and uploaded to a private site the next work day</li>
      <li>2. Your team will have a new understanding of each other’s strengths and weaknesses</li>
      <li>3. Your team will grow in confidence and trust</li>
      <li>4. You’ll have brainstorming skills you can use in your organisation</li>
      <li>5. You’ll build a creative bond to inspire and motivate the group</li>
      <li>6. The video package will showcase the talents of your team and could potentially be used in your organisation to communicate your team’s message</li>
    </ol>
  </section>

  <div class="base-bands" aria-hidden="true">
    <span class="band--lime"></span>
    <span class="band--forest"></span>
    <span class="band--sky"></span>
  </div>
</main>
</body>
</html>
```